Two wall artworks for physiotherapy clinic waiting room

We are a physiotherapy clinic located in Glebe, Sydney. We have a clinic that is within a beautiful heritage listed building and we have two blank white walls that need artwork. Each artwork will be 3000mm wide and 1200mm high. Our clinic is mostly white and I will include our brand's colours below. We are looking for bright, beautiful artworks that are consistent with our colours. One of the artworks should include our full logo including the text so that customers see the name of the clinic on their way into the waiting room. I will include our logo in the files below, as well as images of the clinic, the walls and some other signs that we have already. We would prefer artworks with nice patterns or graphics rather than images of people.

```html
<!DOCTYPE html>
<html lang="en">
<head>
<meta charset="utf-8">
<title>Wattle Physio – Waiting Room Wall Artworks</title>
<link href="https://fonts.googleapis.com/css2?family=Montserrat:wght@500;600&display=swap" rel="stylesheet">
<style>
  :root{
    --backdrop:#a0a0a0;
    --navy:#1e1a6e;
    --deep-navy:#041e50;
    --teal:#12c9b3;
    --teal-dark:#1a7f93;
    --mint:#4deec0;
    --aqua:#36dcd8;
    --paper:#ffffff;
    --paper-soft:#f1f1f1;
  }
  *{margin:0;padding:0;box-sizing:border-box}
  html,body{width:978px;height:1200px;overflow:hidden;background:var(--backdrop)}
  .board{position:relative;width:978px;height:1200px}
  .artwork{position:absolute;left:84px;width:810px;height:324px;overflow:hidden;
    box-shadow:0 22px 40px rgba(0,0,0,.45)}
  .artwork svg{display:block;width:810px;height:324px}
  .artwork--waves{top:78px}
  .artwork--gradient{top:438px}
  .artwork--blobs{top:799px}
  .brand-name{font-family:"Montserrat",sans-serif;font-weight:600}
  .brand-line{font-family:"Montserrat",sans-serif;font-weight:600}
</style>
</head>
<body>
<main class="board">

  <section class="artwork artwork--waves" aria-label="Wall artwork one: teal waves with clinic name">
    <svg viewBox="0 0 810 324" xmlns="http://www.w3.org/2000/svg">
      <defs>
        <linearGradient id="paperFade" x1="0" y1="0" x2="1" y2="1">
          <stop offset="0" stop-color="var(--paper)"/>
          <stop offset="1" stop-color="var(--paper-soft)"/>
        </linearGradient>
        <linearGradient id="tealWave" x1="0" y1="0" x2="1" y2="0.3">
          <stop offset="0" stop-color="var(--teal-dark)"/>
          <stop offset="1" stop-color="#12d9b4"/>
        </linearGradient>
        <linearGradient id="tealWaveLow" x1="0" y1="1" x2="1" y2="0">
          <stop offset="0" stop-color="#14c2b2"/>
          <stop offset="1" stop-color="var(--teal-dark)"/>
        </linearGradient>
        <linearGradient id="orb" x1="0" y1="0" x2="1" y2="1">
          <stop offset="0" stop-color="var(--teal-dark)"/>
          <stop offset="1" stop-color="#16e0bb"/>
        </linearGradient>
        <pattern id="navyDots" width="14.6" height="14.6" patternUnits="userSpaceOnUse">
          <circle cx="1.5" cy="1.5" r="1.4" fill="var(--navy)"/>
        </pattern>
      </defs>
      <rect width="810" height="324" fill="url(#paperFade)"/>
      <path d="M339,0 C360,40 400,70 450,68 C500,66 540,40 580,60 C620,80 610,170 670,190 C710,204 760,185 810,180 L810,0Z" fill="url(#tealWave)"/>
      <path d="M0,170 C40,155 90,160 110,210 C125,250 130,300 150,300 C200,290 250,265 300,270 C340,275 360,300 410,324 L0,324Z" fill="url(#tealWaveLow)"/>
      <rect x="41" y="2" width="61" height="76" fill="url(#navyDots)"/>
      <rect x="709" y="272" width="61" height="47" fill="url(#navyDots)"/>
      <circle cx="476" cy="86" r="11" fill="url(#orb)"/>
      <circle cx="146" cy="202" r="13" fill="url(#orb)"/>
      <circle cx="770" cy="75" r="9.5" fill="none" stroke="#ffffff" stroke-opacity=".7" stroke-width="1.5"/>
      <path d="M664,131 l10,10 M674,131 l-10,10" stroke="#ffffff" stroke-opacity=".7" stroke-width="1.5"/>
      <path d="M49,203 v14 M42,210 h14" stroke="#ffffff" stroke-opacity=".7" stroke-width="1.3"/>
      <circle cx="322" cy="193" r="20" fill="var(--teal)"/>
      <text class="brand-name" x="357" y="199" font-size="36" textLength="238" lengthAdjust="spacingAndGlyphs" fill="var(--navy)">Wattle Physio</text>
      <text class="brand-line" x="359" y="218" font-size="11.4" textLength="234" lengthAdjust="spacingAndGlyphs" fill="var(--navy)">Physiotherapy and Exercise Physiology</text>
    </svg>
  </section>

  <section class="artwork artwork--gradient" aria-label="Wall artwork two: teal to navy gradient">
    <svg viewBox="0 0 810 324" xmlns="http://www.w3.org/2000/svg">
      <defs>
        <linearGradient id="skyToNavy" x1="0" y1="0" x2="0" y2="1">
          <stop offset="0" stop-color="#3fcfc5"/>
          <stop offset=".45" stop-color="#2a8fb0"/>
          <stop offset=".8" stop-color="#1c2a7a"/>
          <stop offset="1" stop-color="#1c1466"/>
        </linearGradient>
        <linearGradient id="softSwell" x1="0" y1="0" x2="1" y2="0">
          <stop offset="0" stop-color="#2a4fa0" stop-opacity=".55"/>
          <stop offset="1" stop-color="#20c6d4" stop-opacity=".5"/>
        </linearGradient>
      </defs>
      <rect width="810" height="324" fill="url(#skyToNavy)"/>
      <path d="M0,70 C60,100 90,110 150,92 C220,72 300,150 380,160 C460,170 540,130 600,150 C650,165 690,160 720,140 C760,110 790,70 810,40 V0 H0Z" fill="#3ecfc5" opacity=".35"/>
      <path d="M380,80 C430,80 500,150 560,155 C620,160 680,150 720,170 C760,190 790,200 810,200 V0 H750 C720,40 690,50 650,45 C600,40 590,70 560,75 C520,80 440,60 380,80Z" fill="url(#softSwell)"/>
      <circle cx="366" cy="285" r="8" fill="none" stroke="#ffffff" stroke-width="2.2"/>
      <text class="brand-name" x="383" y="287" font-size="12" textLength="84" lengthAdjust="spacingAndGlyphs" fill="#ffffff">Wattle Physio</text>
      <text class="brand-line" x="384" y="293.5" font-size="3.6" textLength="83" lengthAdjust="spacingAndGlyphs" fill="#ffffff">Physiotherapy and Exercise Physiology</text>
    </svg>
  </section>

  <section class="artwork artwork--blobs" aria-label="Wall artwork three: navy and aqua blobs with clinic name">
    <svg viewBox="0 0 810 324" xmlns="http://www.w3.org/2000/svg">
      <defs>
        <linearGradient id="aquaMint" x1="0" y1="0" x2="1" y2="0">
          <stop offset="0" stop-color="var(--mint)"/>
          <stop offset="1" stop-color="var(--aqua)"/>
        </linearGradient>
        <linearGradient id="aquaMintLow" x1="0" y1="0" x2="1" y2="0.4">
          <stop offset="0" stop-color="var(--aqua)"/>
          <stop offset="1" stop-color="var(--mint)"/>
        </linearGradient>
        <linearGradient id="aquaOrb" x1="0" y1="1" x2="1" y2="0">
          <stop offset="0" stop-color="var(--aqua)"/>
          <stop offset="1" stop-color="var(--mint)"/>
        </linearGradient>
        <pattern id="whiteDots" width="11.3" height="13" patternUnits="userSpaceOnUse">
          <circle cx="1.3" cy="1.3" r="1.2" fill="#ffffff"/>
        </pattern>
      </defs>
      <rect width="810" height="324" fill="var(--paper)"/>
      <path d="M456,0 C490,25 520,35 560,35 H660 C700,35 690,110 720,135 C740,145 780,142 810,142 V0Z" fill="url(#aquaMint)"/>
      <path d="M0,0 H240 C225,35 190,38 150,40 C100,42 75,60 78,110 C80,160 95,190 55,190 C30,192 10,185 0,180Z" fill="var(--deep-navy)"/>
      <path d="M292,0 H456 C490,25 520,35 560,35 H660 C700,35 690,110 720,135 C740,145 780,142 810,142 V210 C740,220 710,210 690,180 C660,140 640,145 590,160 C540,175 500,160 490,110 C480,60 450,56 400,58 C340,60 300,45 292,0Z" fill="var(--deep-navy)"/>
      <rect x="544" y="37" width="172" height="82" fill="url(#whiteDots)"/>
      <path d="M0,266 C40,266 70,226 110,226 C150,226 180,270 210,300 C240,324 270,295 320,294 C350,293 375,310 390,324 H0Z" fill="url(#aquaMintLow)"/>
      <circle cx="155" cy="92" r="16" fill="url(#aquaOrb)"/>
      <circle cx="510" cy="268" r="20" fill="#3ccac0"/>
      <text class="brand-name" x="541" y="272" font-size="34" textLength="216" lengthAdjust="spacingAndGlyphs" fill="var(--navy)">Wattle Physio</text>
      <text class="brand-line" x="542" y="290" font-size="10.6" textLength="212" lengthAdjust="spacingAndGlyphs" fill="var(--navy)">Physiotherapy and Exercise Physiology</text>
    </svg>
  </section>

</main>
</body>
</html>
```